Start-up lawncare company needing marketing flyer to promote business model

Hello! We are looking for a marketing flyer design with the requirements below.

We would like the size to fit a flyer that is 6.25" X 9", Front and Back.

We need these to meet the NPDS RZDC requirements, there are details attached for the indicias that need to be included, and where to put them on the back of the flyer.

Here's the items items we would like to have included on the flyer:
- Logo (Attached)

- I attached a snip of how our website looks, as well as how our app looks, and would like to follow that general color scheme

- References to our YardPerch App, in both Brindle and Quoll stores, and our website (www.YardPerch.example)

- Reference to the neighborhood barometer and gets the point across that the more of their neighbors that sign up, the cheaper the price of service (Visual attached of what this barometer looks like)

- We are licensed and insured landscaping pros

- Real, instant, upfront pricing for mowing, mulching and most other services

- Sign up with a few easy steps and manage your account from our app or online

- Automated safe & secure transactions upon service completion and satisfaction

- Excellent customer service with our quality guaranteed commitment!

- Sign up now and receive 50% off your first mow!

- Veteran owned

- A portion of our proceeds go to "Rowan Ellery Foundation"

- List's out all of the services we will offer
- Mowing
- Mulching
- Aeration and Over-seeding
- Fertilization
- Shrub/Tree Trimming
- Leaf removal and yard clean up
- Accent lighting installation
- Sprinkler blow-out / Winterization
- Driveway pressure washing and sealing
- Firewood Delivery

Target Market(s)

Homeowners in large neighborhoods that need lawn care services

Industry/Entity Type

Lawn Care

Font styles to use
Sans Serif

Colors

Designer to choose colors to be used in the design.

Requirements
Must have
• Meet NPDS RZDC requirements
• Keep a similar color scheme to our website, feel free to use bold accents to make it more eye-catching as people search through their mail
• Get the general point across that as more of their neighbors sign up with us, the cheaper their service will be

```html
<!DOCTYPE html>
<html lang="en">
<head>
<meta charset="utf-8">
<title>YardPerch Mailer</title>
<link rel="stylesheet" href="https://fonts.googleapis.com/css2?family=Oswald:wght@600;700&family=Cabin:wght@600;700&family=Archivo+Black&family=Arimo:wght@400;700&display=swap">
<style>
  :root {
    --navy: #233f9a;
    --navy-deep: #1f3a94;
    --forest: #1d6b34;
    --leaf: #2ee07f;
    --grass: #6cc04a;
    --sky: #1b87cc;
    --sky-light: #29a8de;
    --ink: #1a1a1a;
    --white: #ffffff;
    --stage: #e9eaec;
    --house-red: #e0644a;
    --house-grey: #9aa9b8;
    --house-orange: #f28a3a;
  }
  * { box-sizing: border-box; margin: 0; padding: 0; }
  html, body { width: 982px; height: 1200px; overflow: hidden; background: var(--stage); }
  body { position: relative; font-family: "Cabin", sans-serif; color: var(--ink); }

  .card {
    position: absolute; left: 113px; width: 756px; height: 548px;
    background: var(--white); overflow: hidden;
    box-shadow: 0 4px 14px rgba(0,0,0,.18);
  }
  .card--front { top: 40px; }
  .card--back { top: 612px; }
  .card__art { position: absolute; inset: 0; width: 756px; height: 548px; }
  .abs { position: absolute; }

  .brand {
    display: flex; align-items: center; gap: 10px;
    font-family: "Cabin", sans-serif; font-weight: 700; font-size: 36px; line-height: 1.2; color: var(--white);
  }
  .brand__dot { width: 24px; height: 24px; border-radius: 50%; background: var(--leaf); }
  .card--front .brand { left: 24px; top: 56px; }
  .card--back .brand { left: 24px; top: 50px; }

  .headline {
    right: 25px; top: 34px; text-align: right; color: var(--navy);
    font-family: "Oswald", sans-serif; font-weight: 700; line-height: 1;
  }
  .headline__top { font-size: 44px; letter-spacing: 0.5px; }
  .headline__bottom { font-size: 33px; font-weight: 600; margin-top: 4px; }

  .offer { left: 360px; top: 157px; color: var(--white); font-weight: 700; line-height: 1; }
  .offer__lead { font-size: 15px; }
  .offer__big { font-family: "Oswald", sans-serif; font-size: 34px; line-height: 0.95; margin: 2px 0 1px; }
  .offer__tail { font-size: 14px; }

  .benefits { left: 22px; top: 260px; list-style: none; }
  .benefits li {
    position: absolute; left: 0; width: 460px; display: flex; gap: 14px;
    font-size: 15.5px; font-weight: 600; line-height: 1.02;
  }
  .benefits svg { flex: none; width: 19px; height: 19px; }

  .url-band {
    font-family: "Cabin", sans-serif; font-weight: 700; color: var(--white);
    font-size: 16px; letter-spacing: 3.6px;
  }
  .card--front .url-band { left: 105px; top: 518px; }
  .card--back .url-band { left: 50px; top: 520px; }

  .phone { left: 560px; top: 138px; width: 172px; height: 352px; }
  .store-badge { left: 446px; width: 107px; height: 32px; border-radius: 5px; background: #000; border: 1px solid #bbb; }

  .services-title {
    left: 24px; top: 258px; color: var(--white);
    font-family: "Cabin", sans-serif; font-weight: 700; font-size: 22px; line-height: 0.98; letter-spacing: -0.3px;
  }
  .services { left: 27px; top: 324px; list-style: none; }
  .services li { font-size: 14.6px; font-weight: 600; line-height: 16.2px; display: flex; }
  .services li::before { content: "•"; width: 27px; color: var(--navy-deep); font-size: 14px; }

  .savings {
    left: 426px; top: 24px; width: 288px; height: 114px; background: var(--grass);
    color: var(--white); font-family: "Archivo Black", sans-serif; font-size: 10.6px;
    text-align: center; line-height: 1.28; padding: 14px 10px 0; text-transform: uppercase;
  }
  .savings p + p { margin-top: 13px; }
  .savings strong { font-size: 14px; }

  .meter { left: 434px; top: 170px; width: 280px; height: 100px; }

  .indicia {
    left: 642px; top: 304px; width: 69px; height: 70px; border: 1px solid var(--ink);
    font-family: "Arimo", sans-serif; font-size: 9.2px; text-align: center; line-height: 11.2px; padding-top: 4px;
  }
  .indicia b { font-weight: 700; }

  .address {
    left: 455px; top: 410px; width: 230px; height: 92px; border: 1px solid var(--ink);
    font-family: "Arimo", sans-serif; font-size: 13px; line-height: 15px;
  }
  .address__route { position: absolute; right: 18px; top: 11px; font-size: 10.5px; }
  .address__name { position: absolute; left: 16px; top: 44px; }
</style>
</head>
<body>

<section class="card card--front" aria-label="Front of mailer">
  <svg class="card__art" viewBox="0 0 756 548" aria-hidden="true">
    <defs>
      <linearGradient id="leafSweep" x1="0" y1="1" x2="1" y2="0">
        <stop offset="0" stop-color="#28c76a"/>
        <stop offset="1" stop-color="#3cf08f"/>
      </linearGradient>
    </defs>
    <path d="M0,0 H505 C340,40 180,140 0,300 Z" fill="var(--forest)"/>
    <path d="M0,318 C170,170 340,50 520,0 H565 C380,35 200,150 0,304 Z" fill="url(#leafSweep)"/>
    <path d="M276,150 H562 V230 H276 L306,190 Z" fill="var(--sky)"/>
    <rect x="0" y="508" width="520" height="40" fill="var(--navy)"/>
    <path d="M380,548 C410,430 540,345 756,325 V548 Z" fill="var(--sky)"/>
    <path d="M420,548 C450,445 570,370 756,352 V548 Z" fill="var(--forest)"/>
    <path d="M540,548 C570,470 650,420 756,410 V548 Z" fill="#1a6230"/>
  </svg>

  <div class="brand abs"><span class="brand__dot"></span>YardPerch</div>

  <h1 class="headline abs">
    <div class="headline__top">YARDPERCH IS A</div>
    <div class="headline__bottom">VETERAN OWNED BUSINESS</div>
  </h1>

  <div class="offer abs">
    <div class="offer__lead">Sign up now and receive</div>
    <div class="offer__big">50% off</div>
    <div class="offer__tail">your first mow!</div>
  </div>

  <ul class="benefits abs">
    <li style="top:0px"><svg viewBox="0 0 20 20"><circle cx="10" cy="10" r="8.6" fill="none" stroke="var(--navy)" stroke-width="1.8"/><path d="M5.8,10.4 L8.8,13.2 L14.4,6.8" fill="none" stroke="var(--navy)" stroke-width="2.2"/></svg><span>We are licensed and insured landscaping pros</span></li>
    <li style="top:22px"><svg viewBox="0 0 20 20"><circle cx="10" cy="10" r="8.6" fill="none" stroke="var(--navy)" stroke-width="1.8"/><path d="M5.8,10.4 L8.8,13.2 L14.4,6.8" fill="none" stroke="var(--navy)" stroke-width="2.2"/></svg><span>Real, instant, upfront pricing for mowing, mulching and<br>most other services</span></li>
    <li style="top:61px"><svg viewBox="0 0 20 20"><circle cx="10" cy="10" r="8.6" fill="none" stroke="var(--navy)" stroke-width="1.8"/><path d="M5.8,10.4 L8.8,13.2 L14.4,6.8" fill="none" stroke="var(--navy)" stroke-width="2.2"/></svg><span>Sign up with a few easy steps and manage your account<br>from our app or online</span></li>
    <li style="top:99px"><svg viewBox="0 0 20 20"><circle cx="10" cy="10" r="8.6" fill="none" stroke="var(--navy)" stroke-width="1.8"/><path d="M5.8,10.4 L8.8,13.2 L14.4,6.8" fill="none" stroke="var(--navy)" stroke-width="2.2"/></svg><span>Automated safe &amp; secure transactions upon service<br>completion and satisfaction</span></li>
    <li style="top:137px"><svg viewBox="0 0 20 20"><circle cx="10" cy="10" r="8.6" fill="none" stroke="var(--navy)" stroke-width="1.8"/><path d="M5.8,10.4 L8.8,13.2 L14.4,6.8" fill="none" stroke="var(--navy)" stroke-width="2.2"/></svg><span>Excellent customer service with our quality<br>guaranteed commitment!</span></li>
    <li style="top:178px"><svg viewBox="0 0 20 20"><circle cx="10" cy="10" r="8.6" fill="none" stroke="var(--navy)" stroke-width="1.8"/><path d="M5.8,10.4 L8.8,13.2 L14.4,6.8" fill="none" stroke="var(--navy)" stroke-width="2.2"/></svg><span>Veteran owned</span></li>
    <li style="top:203px"><svg viewBox="0 0 20 20"><circle cx="10" cy="10" r="8.6" fill="none" stroke="var(--navy)" stroke-width="1.8"/><path d="M5.8,10.4 L8.8,13.2 L14.4,6.8" fill="none" stroke="var(--navy)" stroke-width="2.2"/></svg><span>A portion of our proceeds go to<br>"Rowan Ellery Foundation"</span></li>
  </ul>

  <div class="store-badge abs" style="top:426px" role="img" aria-label="Quoll Store download badge"></div>
  <div class="store-badge abs" style="top:462px" role="img" aria-label="Brindle Store download badge"></div>

  <svg class="phone abs" viewBox="0 0 172 352" role="img" aria-label="Phone showing the YardPerch instant quote screen at quote.yardperch.example">
    <defs>
      <linearGradient id="screenTone" x1="0" y1="0" x2="0" y2="1">
        <stop offset="0" stop-color="#3aa85c"/>
        <stop offset="0.7" stop-color="#e8efe9"/>
        <stop offset="1" stop-color="#2a56b0"/>
      </linearGradient>
    </defs>
    <rect x="0" y="0" width="172" height="352" rx="20" fill="#1b1b1b"/>
    <rect x="6" y="8" width="160" height="336" rx="15" fill="url(#screenTone)"/>
  </svg>

  <div class="url-band abs">www.YardPerch.example</div>
</section>

<section class="card card--back" aria-label="Back of mailer">
  <svg class="card__art" viewBox="0 0 756 548" aria-hidden="true">
    <defs>
      <linearGradient id="leafSweepBack" x1="0" y1="1" x2="1" y2="0">
        <stop offset="0" stop-color="#28c76a"/>
        <stop offset="1" stop-color="#3cf08f"/>
      </linearGradient>
    </defs>
    <path d="M0,0 H500 C340,40 170,150 40,246 H0 Z" fill="var(--forest)"/>
    <path d="M40,246 C170,140 360,40 540,0 H585 C380,45 200,150 58,246 Z" fill="url(#leafSweepBack)"/>
    <path d="M0,246 H360 A34,34 0 0 1 360,314 H0 Z" fill="var(--navy-deep)"/>
    <rect x="0" y="510" width="396" height="38" fill="var(--sky-light)"/>
  </svg>

  <div class="brand abs"><span class="brand__dot"></span>YardPerch</div>

  <h2 class="services-title abs">LIST'S OUT ALL OF THE SERVICES<br>WE WILL OFFER</h2>

  <ul class="services abs">
    <li>Mowing</li>
    <li>Mulching</li>
    <li>Aeration and Over-seeding</li>
    <li>Fertilization</li>
    <li>Shrub/Tree Trimming</li>
    <li>Leaf removal and yard clean up</li>
    <li>Accent lighting installation</li>
    <li>Sprinkler blow-out / Winterization</li>
    <li>Driveway pressure washing and sealing</li>
    <li>Firewood Delivery</li>
  </ul>

  <div class="savings abs">
    <p>You could save up to <strong>10%</strong> off our already low prices, as more of your neighbors sign up!</p>
    <p>Check out our app today to see how much your neighbors are already saving!</p>
  </div>

  <svg class="meter abs" viewBox="0 0 280 100" role="img" aria-label="Neighborhood savings meter from 0% to 10%">
    <defs>
      <linearGradient id="meterFill" x1="0" y1="0" x2="1" y2="0">
        <stop offset="0" stop-color="var(--house-red)"/>
        <stop offset="0.5" stop-color="var(--house-grey)"/>
        <stop offset="1" stop-color="var(--house-orange)"/>
      </linearGradient>
    </defs>
    <path d="M17,48 L35,34 L53,48 H48 V64 H22 V48 Z" fill="var(--house-red)"/>
    <rect x="31" y="54" width="8" height="10" fill="#fff"/>
    <rect x="42" y="51" width="4" height="4" fill="#fff"/>
    <path d="M100,38 L126,18 L152,38 H145 V64 H107 V38 Z" fill="var(--house-grey)"/>
    <rect x="119" y="50" width="10" height="14" fill="#fff"/>
    <rect x="133" y="48" width="6" height="6" fill="#fff"/>
    <path d="M188,34 L222,4 L256,34 H248 V64 H196 V34 Z" fill="var(--house-orange)"/>
    <rect x="210" y="46" width="13" height="18" fill="#fff"/>
    <rect x="230" y="44" width="9" height="9" fill="#fff"/>
    <rect x="0" y="68" width="272" height="23" rx="11.5" fill="#e6e6e6"/>
    <rect x="0" y="68" width="222" height="23" rx="11.5" fill="url(#meterFill)"/>
    <text x="126" y="85" text-anchor="middle" font-family="Archivo Black, sans-serif" font-size="13" fill="#fff">5%</text>
    <text x="244" y="85" text-anchor="middle" font-family="Archivo Black, sans-serif" font-size="13" fill="#fff">10%</text>
  </svg>

  <div class="indicia abs">PRSRT STD<br>ECRWSS<br>U.S. Postage<br><b>PAID</b><br>RZDC RETAIL</div>

  <div class="address abs">
    <span class="address__route">*****************ECRWSS****</span>
    <span class="address__name">Local<br>Postal Customer</span>
  </div>

  <div class="url-band abs">www.YardPerch.example</div>
</section>

</body>
</html>
```